Expensive Jewelery and Gold Website

I require a one page template design for my site PrimeIngotHouse.net. We sell replica gold bars. Not real ones, they are novelty gifts.

I have several images of the bars (attached)
I would like a stylish and professional template layout that will be used on my site.

Designed to appear to businesses and professionals and not the members of the public.

There is no idenity or artwork for the business so you may use whichever scheme you wish to. But must somehow stylish use the images or 2-3 of the images attached.

Target Market(s)

Business and marketing professional.

Industry/Entity Type

Business

Requirements
Must have
• Incorporate some or all of images
Nice to have
• Colour/styled images to match design and look in-keeping

```html
<!DOCTYPE html>
<html lang="en">
<head>
<meta charset="utf-8">
<title>PrimeIngotHouse.net</title>
<link rel="stylesheet" href="https://fonts.googleapis.com/css2?family=Arimo:wght@400;700&display=swap">
<style>
:root{
  --topbar:#6e1208;
  --header-top:#b51f0c;
  --header-bottom:#7a150d;
  --band:#0c0505;
  --frame:#111;
  --cream-top:#e2dbb9;
  --cream-bottom:#f8f5ea;
  --heading:#5a1106;
  --body:#5a1106;
  --link:#c0260f;
  --rule:#9b5a3c;
  --tick:#e8402a;
  --footer-top:#6c0f06;
  --footer-bottom:#7e1a12;
  --white:#fff;
}
*{margin:0;padding:0;box-sizing:border-box}
html,body{width:1200px;height:1187px;overflow:hidden}
body{position:relative;font-family:"Arimo",Arial,sans-serif;background:var(--cream-bottom)}
.top-strip{position:absolute;left:0;top:0;width:1200px;height:12px;background:var(--topbar)}
.header{position:absolute;left:0;top:12px;width:1200px;height:464px;background:linear-gradient(var(--header-top),var(--header-bottom) 45%,var(--header-bottom))}
.header-band{position:absolute;left:0;top:476px;width:1200px;height:10px;background:var(--band);border-bottom:2px solid #fff}
.showcase{position:absolute;left:77px;top:79px;width:1075px;height:339px;background:var(--frame);border-radius:26px}
.photo{position:absolute;border-radius:10px}
.photo-case{left:12px;top:12px;width:403px;height:315px;background:linear-gradient(135deg,#2a1a12,#8a5a2e 40%,#1b1512 70%,#b07a3a);border-radius:12px 0 0 12px}
.photo-gift{left:636px;top:12px;width:427px;height:315px;background:linear-gradient(135deg,#8f8780,#cfcbc6 50%,#a49b93);border-radius:0 12px 12px 0}
.brand-tab{position:absolute;left:492px;top:31px;width:221px;height:384px;border:3px solid #000;border-radius:16px;background:linear-gradient(#7a1f1a,#3a0d0a 45%,#0a0707 75%,#111)}
.brand-name{position:absolute;left:0;top:58px;width:100%;text-align:center;font-weight:700;font-size:22px;color:#f2a311;letter-spacing:.2px}
.photo-bar{left:24px;top:110px;width:168px;height:255px;background:linear-gradient(160deg,#3a2a10,#c58d1e 45%,#6a4a14 75%,#1a1208);border-radius:6px}
.nav{position:absolute;left:0;top:436px;width:1200px;text-align:center;font-size:17px;color:var(--white)}
.nav a{color:var(--white);text-decoration:none;padding:1px 3px}
.nav a.current{background:#b3401d}
.nav .sep{margin:0 8px}
.content{position:absolute;left:0;top:488px;width:1200px;height:606px;background:linear-gradient(var(--cream-top),var(--cream-bottom) 75%)}
.article{position:absolute;left:90px;width:768px;color:var(--body)}
.article h2{font-size:27px;font-weight:700;color:var(--heading);text-shadow:1px 1px 0 rgba(0,0,0,.15);margin-bottom:8px;letter-spacing:.2px}
.article p{font-size:13px;line-height:17.4px;margin-bottom:4px}
.read-more{display:block;text-align:right;font-size:13.5px;color:var(--link);text-decoration:none;padding-right:16px;margin-top:6px}
.article-one{top:22px}
.article-two{top:300px}
.divider{position:absolute;left:97px;top:256px;width:748px;border-top:1px dashed var(--rule)}
.sidebar{position:absolute;left:926px;top:22px;width:190px}
.sidebar h3{font-size:29px;font-weight:700;color:var(--heading);text-shadow:1px 1px 0 rgba(0,0,0,.15);margin-bottom:8px}
.categories{list-style:none}
.categories li{position:relative;height:36.4px;padding:12px 0 0 26px;font-size:14.5px;letter-spacing:1px;color:#2a1a14;border-bottom:1px dashed #6e2a1a;margin-left:10px;padding-left:16px}
.categories li svg{position:absolute;left:-11px;top:8px}
.footer{position:absolute;left:0;top:1094px;width:1200px;height:93px;background:linear-gradient(var(--footer-top),var(--footer-bottom))}
.footer-nav{position:absolute;left:68px;top:36px;font-size:14.4px;color:var(--white)}
.footer-nav a{color:var(--white);text-decoration:none}
.footer-nav .sep{margin:0 9px}
.copyright{position:absolute;right:36px;top:36px;font-size:14px;color:var(--white)}
</style>
</head>
<body>
<div class="top-strip"></div>
<header class="header"></header>
<div class="header-band"></div>

<div class="showcase">
  <div class="photo photo-case" role="img" aria-label="Gold bar resting in a velvet-lined presentation case"></div>
  <div class="photo photo-gift" role="img" aria-label="Gift box wrapped in silver paper with a sheer ribbon bow"></div>
</div>
<div class="brand-tab">
  <div class="brand-name">PrimeIngotHouse</div>
  <div class="photo photo-bar" role="img" aria-label="Close-up of a gold bar in a clear capsule"></div>
</div>

<nav class="nav">
  <a class="current" href="#">Home</a><span class="sep">|</span><a href="#">Register</a><span class="sep">|</span><a href="#">Login</a><span class="sep">|</span><a href="#">Media</a><span class="sep">|</span><a href="#">Jobs</a><span class="sep">|</span><a href="#">Contact</a><span class="sep">&nbsp;|</span><a href="#">About us</a><span class="sep">|</span><a href="#">Sitemap</a>
</nav>

<main class="content">
  <article class="article article-one">
    <h2>Keeping Your Gold Bullion Safe</h2>
    <p>A popular way to beat the rapidly changing turmoil of today's economy is to invest in gold. Gold can come in bars or coins. Most people might think of the bars type when they hear the phrase, gold bullion. However, it can be in the form of coins as well. Most times it is not really safe to keep your gold at home. At one time, people would save their money by placing it under the mattress. This is not a very good place to keep your gold bullion, besides it would make your bed pretty uncomfortable.</p>
    <p>Some people who do keep their gold bullion at home, have a safe or some special vault-like object to save the gold in. Other people keep their gold in bank vaults or safety deposit boxes. These are often safe places to keep gold but you do not have the access to the gold as quickly as some people might wish. Fortunately there are other options to consider as well.</p>
    <a class="read-more" href="#">Read More</a>
  </article>
  <div class="divider"></div>
  <article class="article article-two">
    <h2>Some abcs on Gold Bullion Trading</h2>
    <p>If you have thought about trading in gold bullion but were not sure of what is involved, here is some information to help you make the right decision. First, gold bullion can be bought or sold just like any other product that can be traded on the market. Some companies deal exclusively in gold because of possible profits that can be earned.</p>
    <p>Most people who purchase gold do so at wholesale prices and then turn it around to sell to gold dealers, jewellers, and others who need gold as a material. Buying gold in large quantities (wholesale) and breaking it up to sell in smaller pieces can be very profitable. First, you find a seller who will deal in wholesale prices and then you take the time to break it up so that it can be sold in smaller quantities. You can get the cheaper price because it is purchased in bulk form.</p>
    <a class="read-more" href="#" style="margin-top:20px">Read More</a>
  </article>

  <aside class="sidebar">
    <h3>Categories</h3>
    <ul class="categories">
      <li><svg width="20" height="18" viewBox="0 0 20 18"><path d="M2 9l5 6L18 2" fill="none" stroke="var(--tick)" stroke-width="3.5" stroke-linecap="round" stroke-linejoin="round"/></svg>British Gold</li>
      <li><svg width="20" height="18" viewBox="0 0 20 18"><path d="M2 9l5 6L18 2" fill="none" stroke="var(--tick)" stroke-width="3.5" stroke-linecap="round" stroke-linejoin="round"/></svg>Bullion Coins</li>
      <li><svg width="20" height="18" viewBox="0 0 20 18"><path d="M2 9l5 6L18 2" fill="none" stroke="var(--tick)" stroke-width="3.5" stroke-linecap="round" stroke-linejoin="round"/></svg>Bullion Vault</li>
      <li><svg width="20" height="18" viewBox="0 0 20 18"><path d="M2 9l5 6L18 2" fill="none" stroke="var(--tick)" stroke-width="3.5" stroke-linecap="round" stroke-linejoin="round"/></svg>Fake</li>
      <li><svg width="20" height="18" viewBox="0 0 20 18"><path d="M2 9l5 6L18 2" fill="none" stroke="var(--tick)" stroke-width="3.5" stroke-linecap="round" stroke-linejoin="round"/></svg>F<span style="font-size:11.5px">AQ</span></li>
      <li><svg width="20" height="18" viewBox="0 0 20 18"><path d="M2 9l5 6L18 2" fill="none" stroke="var(--tick)" stroke-width="3.5" stroke-linecap="round" stroke-linejoin="round"/></svg>Fort Knox</li>
      <li><svg width="20" height="18" viewBox="0 0 20 18"><path d="M2 9l5 6L18 2" fill="none" stroke="var(--tick)" stroke-width="3.5" stroke-linecap="round" stroke-linejoin="round"/></svg>Fraud</li>
      <li><svg width="20" height="18" viewBox="0 0 20 18"><path d="M2 9l5 6L18 2" fill="none" stroke="var(--tick)" stroke-width="3.5" stroke-linecap="round" stroke-linejoin="round"/></svg>Gold</li>
      <li><svg width="20" height="18" viewBox="0 0 20 18"><path d="M2 9l5 6L18 2" fill="none" stroke="var(--tick)" stroke-width="3.5" stroke-linecap="round" stroke-linejoin="round"/></svg>Gold Bars</li>
      <li><svg width="20" height="18" viewBox="0 0 20 18"><path d="M2 9l5 6L18 2" fill="none" stroke="var(--tick)" stroke-width="3.5" stroke-linecap="round" stroke-linejoin="round"/></svg>Gold Bullion</li>
      <li style="height:40px;padding-top:16px"><svg width="20" height="18" viewBox="0 0 20 18" style="top:11px"><path d="M2 9l5 6L18 2" fill="none" stroke="var(--tick)" stroke-width="3.5" stroke-linecap="round" stroke-linejoin="round"/></svg>Gold Bullion Trading</li>
      <li><svg width="20" height="18" viewBox="0 0 20 18"><path d="M2 9l5 6L18 2" fill="none" stroke="var(--tick)" stroke-width="3.5" stroke-linecap="round" stroke-linejoin="round"/></svg>Gold Guide</li>
    </ul>
  </aside>
</main>

<footer class="footer">
  <nav class="footer-nav">
    <a href="#">Home</a><span class="sep">|</span><a href="#">Register</a><span class="sep">|</span><a href="#">Login</a><span class="sep">|</span><a href="#">Media</a><span class="sep">|</span><a href="#">Jobs</a><span class="sep">|</span><a href="#">Contact</a><span class="sep">&nbsp;|</span><a href="#">About us</a><span class="sep">|</span><a href="#">Sitemap</a>
  </nav>
  <div class="copyright">&copy; Copyright 2010-2011 &nbsp;PrimeIngotHouse &nbsp;. All Right Reserved</div>
</footer>
</body>
</html>
```